Gas utility and appliance store needs awesome web design

Hearthline Supply is a South African based brick and mortar shop looking to improve it's on-line presence.
We cover the whole gambit or products, appliances, information, services, installations and utility related to domestic gas (in SA still considered an alternative fuel) with our most important offerings being the sale of the gas (LPG) itself in combination with high end kitchen and household gas based appliances (stoves, cookers, heaters, fireplaces etc)
Wesite needs to portray our professional (been in the market since 47), family owned (3'rd gen now) roots - it should create the impression of a market leader - and must also portray our domestic (read man in the street) focus and practical approach.
Something professional but light-hearted enough for the general public.
Design must reinforce the belief that LPG is a green,safe and affordable fuel option for domestic use

Target Market(s)

upper middle class market 25-70

Industry/Entity Type

Appliance

Requirements
Must have
• landing page
our company
sustainability
contact us page
menu bar with links to pages (shop, specific information etc)

```html
<!DOCTYPE html>
<html lang="en">
<head>
<meta charset="utf-8">
<title>Hearthline Supply</title>
<link rel="stylesheet" href="https://fonts.googleapis.com/css2?family=Ubuntu:wght@500;700&family=Arimo:wght@400;700&family=Questrial&display=swap">
<style>
:root{
  --blue:#1e93d2;
  --blue-dark:#0d78b8;
  --blue-light:#5bbbe9;
  --ink:#3f4a56;
  --grey:#6b7178;
  --line:#e3e6e9;
  --footer:#15232c;
  --footer-text:#9aa5ad;
  --page:#ffffff;
}
*{box-sizing:border-box;margin:0;padding:0}
html,body{width:1125px;height:1200px;overflow:hidden;background:var(--page)}
body{position:relative;font-family:"Arimo",Arial,sans-serif;color:var(--ink)}
.abs{position:absolute}
.top-area{left:0;top:0;width:1125px;height:451px;background:#fafbfc;border-top:4px solid var(--blue)}
.band{left:0;top:451px;width:1125px;height:35px;background:linear-gradient(#2a9bd8,#57b5e6)}
/* nav */
.nav-home{left:416px;top:0;width:73px;height:56px;background:var(--blue);color:#fff;font:700 13px "Ubuntu",sans-serif;text-align:center;padding-top:32px;box-shadow:0 6px 6px -4px rgba(0,0,0,.25)}
.nav-home svg{position:absolute;left:27px;top:8px}
.nav-link{top:31px;font:500 13px "Ubuntu",sans-serif;color:#4d5660;transform:translateX(-50%)}
.nav-sep{top:22px;width:1px;height:34px;background:#e4e7ea}
/* brand */
.brand-dot{left:106px;top:58px;width:46px;height:46px;border-radius:50%;background:var(--blue)}
.brand-name{left:162px;top:52px;font:700 28px/1.05 "Ubuntu",sans-serif;color:var(--blue);width:200px}
/* follow */
.follow{left:750px;top:108px;font:500 17px "Ubuntu",sans-serif;color:#555d66}
.social{top:103px;width:30px;height:30px;border-radius:50%}
/* intro */
.intro-kicker{left:105px;top:170px;font:500 19px "Ubuntu",sans-serif;color:var(--blue)}
.intro-title{left:105px;top:195px;font:700 27px "Ubuntu",sans-serif;color:var(--blue)}
.intro-text{left:104px;top:236px;width:255px;font-size:11.5px;line-height:18.7px;color:#555;text-align:justify;letter-spacing:.4px}
.intro-text b{color:#333}
.btn-more{left:98px;top:375px;width:141px;height:37px;border-radius:7px;background:linear-gradient(#5ec0ee,#1b8fd0);color:#fff;font:700 16px "Ubuntu",sans-serif;padding:9px 0 0 11px;box-shadow:0 6px 6px -3px rgba(0,0,0,.2)}
.btn-more span{display:inline-block;width:20px;height:20px;border-radius:50%;background:#fff;vertical-align:-4px;margin-left:4px;position:relative}
.btn-more span:after{content:"";position:absolute;left:8px;top:6px;border-left:6px solid var(--blue);border-top:4px solid transparent;border-bottom:4px solid transparent}
/* hero */
.hero-frame{left:372px;top:141px;width:629px;height:393px;background:#fff;border:1px solid #eceef0;box-shadow:0 14px 14px -10px rgba(0,0,0,.18)}
.hero-photo{left:387px;top:156px;width:604px;height:365px;background:linear-gradient(100deg,#1c2a44 0%,#6a6440 30%,#283650 55%,#4c5a70 75%,#1b2230 100%)}
.slider-tab{left:1001px;top:451px;width:28px;height:84px;background:#3f97d3}
.dot{left:1009px;width:12px;height:12px;border-radius:50%;background:#2a6f8c}
.dot.on{background:#fff}
/* cards */
.card{top:577px;width:211px;height:150px;border-radius:12px;background:linear-gradient(#fff,#ececec);border:1px solid #eceef0;padding:11px 0 0 16px;box-shadow:0 10px 10px -8px rgba(0,0,0,.2)}
.card h3{font:500 17px "Ubuntu",sans-serif;color:var(--blue);margin:0 0 5px 6px}
.card li{list-style:none;font-size:11.5px;color:#555;line-height:20.6px;padding-left:16px;position:relative}
.card li:before{content:"";position:absolute;left:1px;top:5px;width:4px;height:8px;border:solid var(--blue);border-width:0 2.5px 2.5px 0;transform:rotate(40deg)}
.card.active{background:linear-gradient(#63c0ec,#0c7bbf);border-color:#3a9fd8}
.card.active h3,.card.active li{color:#fff}
.card.active li:before{border-color:#fff}
/* blog */
.blog-title{left:118px;top:789px;font:500 18px "Ubuntu",sans-serif;color:#4a5460}
.blog-rule{left:118px;top:820px;width:900px;height:1px;background:var(--line)}
.share{top:787px;height:18px;border:1px solid #cfd5da;border-radius:2px;background:#f3f6f8;font:700 10px "Arimo",sans-serif;color:#3b6ea8;padding:2px 6px}
.count{top:787px;height:18px;border:1px solid #cfd5da;border-radius:2px;background:#fff;font-size:10px;color:#444;padding:2px 6px}
.post{top:834px;width:270px}
.post h4{font:400 16px "Questrial",sans-serif;color:#3f4a56}
.post time{display:block;font-size:11.5px;color:#555;margin:6px 0 11px}
.post p{font-size:12.3px;line-height:19.7px;color:#777}
.post a{font-weight:700;font-style:italic;color:#3d5b86;text-decoration:none}
.blog-shadow{left:180px;top:975px;width:760px;height:2px;background:radial-gradient(ellipse at center,rgba(0,0,0,.12),transparent 70%)}
/* footer */
.footer{left:0;top:998px;width:1125px;height:202px;background:linear-gradient(#1c2e38,#0f1b22);border-top:4px solid var(--blue)}
.f-head{top:1026px;font:700 20px "Ubuntu",sans-serif;color:#fff;letter-spacing:.5px}
.f-item{font-size:11px;line-height:14px;color:var(--footer-text);width:150px}
.f-item span{color:#fff}
.f-sep{height:1px;width:170px;background:#2a3b45}
.f-icon{width:14px;height:12px}
.map{left:797px;top:1084px;width:103px;height:102px;border:3px solid #dfe4e8;background:linear-gradient(135deg,#e8efe3,#cfdcc9 60%,#e6ebe0)}
</style>
</head>
<body>
<div class="abs top-area"></div>
<div class="abs band"></div>

<header>
  <div class="abs brand-dot"></div>
  <div class="abs brand-name">Hearthline<br>Supply</div>

  <nav>
    <div class="abs nav-home">
      <svg width="20" height="18" viewBox="0 0 20 18"><path d="M10 1 1 9h3v8h4v-5h4v5h4V9h3z" fill="#fff"/></svg>HOME
    </div>
    <div class="abs nav-sep" style="left:505px"></div>
    <div class="abs nav-link" style="left:552px">ABOUT</div>
    <div class="abs nav-sep" style="left:610px"></div>
    <div class="abs nav-link" style="left:664px">SHOP</div>
    <div class="abs nav-sep" style="left:712px"></div>
    <div class="abs nav-link" style="left:809px">SPECIFIC INFORMATION</div>
    <div class="abs nav-sep" style="left:912px"></div>
    <div class="abs nav-link" style="left:984px">CONTACT US</div>
  </nav>

  <div class="abs follow">Follow us on :</div>
  <div class="abs social" style="left:863px;background:#d8361e"></div>
  <div class="abs social" style="left:901px;background:#2c5fa8"></div>
  <div class="abs social" style="left:939px;background:#4fb0e2"></div>
  <div class="abs social" style="left:978px;background:#2e5a9a"></div>
</header>

<section class="intro">
  <div class="abs intro-kicker">LPG FIRE - FIRE SUPPRESSION</div>
  <h1 class="abs intro-title">SYSTEMS</h1>
  <p class="abs intro-text"><b>Lorem Ipsum is simply dummy text of the printing and typesetting</b> industry. Lorem Ipsum has been the industry's standard dummy text ever since the 1500s, when an unknown printer took a galley of type and scrambled it to make a type specimen book.</p>
  <div class="abs btn-more">MORE INFO<span></span></div>
</section>

<div class="abs hero-frame"></div>
<div class="abs hero-photo" role="img" aria-label="Gas technician in safety glasses working beside an illuminated refinery at night"></div>
<div class="abs slider-tab"></div>
<div class="abs dot" style="top:462px"></div>
<div class="abs dot on" style="top:486px"></div>
<div class="abs dot" style="top:509px"></div>

<section class="cards">
  <div class="abs card active" style="left:106px"><h3>For My Home</h3><ul><li>e-Bill Paperless Billing</li><li>Saving Energy</li><li>Rates &amp; Programs</li><li>Energy Assistance</li><li>Safety</li></ul></div>
  <div class="abs card" style="left:338px"><h3>For My Business</h3><ul><li>Saving Energy</li><li>e-Bill Paperless Billing</li><li>Energy Information System</li><li>Lakeside Gas Choice</li></ul></div>
  <div class="abs card" style="left:572px"><h3>Energy Efficiency</h3><ul><li>Builders &amp; Contractors</li><li>Educators &amp; Students</li><li>Economic Development</li><li>Landlord Revert Agreement</li></ul></div>
  <div class="abs card" style="left:806px"><h3>Natural Gas Safety</h3><ul><li>About HLS</li><li>Job Opportunities</li><li>Helping the Community</li><li>Helping the Environment</li><li>Regulatory Information</li></ul></div>
</section>

<section class="blog">
  <h2 class="abs blog-title">From Our Blog</h2>
  <div class="abs share" style="left:804px">+1</div>
  <div class="abs count" style="left:836px">0</div>
  <div class="abs share" style="left:871px">Post</div>
  <div class="abs count" style="left:927px">0</div>
  <div class="abs share" style="left:972px">Like</div>
  <div class="abs blog-rule"></div>
  <article class="abs post" style="left:118px"><h4>Lorem ipsum Dolor</h4><time>27. 11. 2011</time><p>Lorem ipsum dolor sit amet, consectetur adipisicing elit, sed do eiusmod tempor incididunt ut labore et dolore magna... <a href="#">read more</a></p></article>
  <article class="abs post" style="left:427px"><h4>Lorem ipsum Dolor</h4><time>27. 11. 2011</time><p>Lorem ipsum dolor sit amet, consectetur adipisicing elit, sed do eiusmod tempor incididunt ut labore et dolore magna... <a href="#">read more</a></p></article>
  <article class="abs post" style="left:727px"><h4>Lorem ipsum Dolor</h4><time>27. 11. 2011</time><p>Lorem ipsum dolor sit amet, consectetur adipisicing elit, sed do eiusmod tempor incididunt ut labore et dolore magna... <a href="#">read more</a></p></article>
  <div class="abs blog-shadow"></div>
</section>

<footer>
  <div class="abs footer"></div>
  <h3 class="abs f-head" style="left:138px">Community</h3>
  <h3 class="abs f-head" style="left:374px">Updates</h3>
  <h3 class="abs f-head" style="left:591px">Contact Us</h3>
  <h3 class="abs f-head" style="left:804px">Map</h3>

  <svg class="abs f-icon" style="left:127px;top:1084px" viewBox="0 0 14 12"><rect x="0" y="5" width="3" height="7" fill="#9aa5ad"/><path d="M4 5 7 0h2v4h4l-1 8H4z" fill="#9aa5ad"/></svg>
  <div class="abs f-item" style="left:152px;top:1083px">The Value Of Links: Part II<br><span>http://lnk.to/hs4kQ</span></div>
  <div class="abs f-sep" style="left:127px;top:1117px"></div>
  <div class="abs f-item" style="left:152px;top:1123px">55 Minimal Black and White Web Designs to Inspire<br><span>You http://lnk.to/hs7mR</span></div>

  <svg class="abs f-icon" style="left:351px;top:1084px" viewBox="0 0 14 12"><path d="M0 2q4 5 8 3l6-4-3 5q-2 5-7 4z" fill="#9aa5ad"/></svg>
  <div class="abs f-item" style="left:377px;top:1083px">The Value Of Links: Part II<br><span>http://lnk.to/hs4kQ</span></div>
  <div class="abs f-sep" style="left:351px;top:1117px"></div>
  <svg class="abs f-icon" style="left:351px;top:1127px" viewBox="0 0 14 12"><path d="M0 2q4 5 8 3l6-4-3 5q-2 5-7 4z" fill="#9aa5ad"/></svg>
  <div class="abs f-item" style="left:377px;top:1123px">55 Minimal Black and White Web Designs to Inspire<br><span>You http://lnk.to/hs7mR</span></div>

  <svg class="abs f-icon" style="left:583px;top:1084px" viewBox="0 0 14 12"><path d="M7 0 0 6h2v6h4V8h2v4h4V6h2z" fill="#9aa5ad"/></svg>
  <div class="abs f-item" style="left:601px;top:1081px;width:170px">48 Ridgeway Hill Rd.<br>Unit 3C, Maple Bend,<br><span>ZA 4120</span></div>
  <div class="abs f-sep" style="left:583px;top:1124px"></div>
  <svg class="abs f-icon" style="left:583px;top:1134px" viewBox="0 0 14 12"><path d="M1 3q6-5 12 0l-1 2-3-1V3H5v1L2 5z M3 6h8l1 6H2z" fill="#9aa5ad"/></svg>
  <div class="abs f-item" style="left:601px;top:1132px;width:170px">Office: 021.555.0147,<br>Cell/Dale<br><span>Nolan: 021.555.0193</span></div>

  <div class="abs map" role="img" aria-label="Street map showing the shop location"></div>
  <div class="abs f-item" style="left:910px;top:1083px;width:90px">The Value Of Links:<br>Part II<br><span>http://lnk.to/hs</span></div>
  <div class="abs f-item" style="left:910px;top:1148px;width:90px">55 Minimal Black White Designs</div>
</footer>
</body>
</html>
```